Rapidly-Growing OTA Needs Catchy Banners in HTML5!

We need simple catchy banners in HTML5!

Wingmerry is a global startup, an online travel agent selling flights. Our technology allows us to combine low-cost and traditional carriers and thus create unique routes not offered by any other OTA. And often up to 90% cheaper!

We want you to create an elegant banner with simple, not overly intrusive, animation, that calls for action.

Goals for the banner - click-through action and building brand awareness.

7 Sizes:

300x250
336x280
728x90
480x60
120x600
160x600
300x600

Provide the animated version in HTML5 + standard picture for each size.

Please, keep the file size of animated .zip down to max 150 kB and picture size to 40kB!

Can contain slides. (e.g. Attention-catching text => animation => logo with call-to-action etc).

Logo (in various sizes) attached.
Font used in for Wingmerry name - Gotham Rounded.
Use Sans Serif.

Text variations attached - you can edit it, add more, if you come up with a better one - plus points :-) But don't digress from the idea of cheap flights. And keep it simple.

Choose the animations as you wish, but simple and professional (merro, the bird maskot, can "fly", clouds can move.. it's up to you).

Creativity and catchiness is the most important aspect!

Logo (merro) with our name, short slogan and a strong call-to-action is a must. The design should evoke flying - up to you how (clouds, sky, shades of blue, etc.)

Our website is newly redesigned in material design and banners should correspond with colors used. www.wingmerry-example.com

Possible long-term cooperation, if the job is well done!

Target Market(s)

Travel segment, portals, blogs, travellers

Industry/Entity Type

Travel Industry

Font styles to use
Sans Serif

Requirements
Must have
• Logo
• Slogan
• Call-to-action
• Elegant animation
• Correspond with brand (www.wingmerry-example.com)
Should not have
• Intrusive animations
• Too long messages

```html
<!DOCTYPE html>
<html lang="en">
<head>
<meta charset="utf-8">
<title>Wingmerry – Find the cheapest flights</title>
<link rel="stylesheet" href="https://fonts.googleapis.com/css2?family=Open+Sans:wght@700;800&display=swap">
<style>
  :root {
    --sky-light: #3f74b4;
    --sky-mid: #1f477f;
    --sky-deep: #0d1c38;
    --badge: #1e2f4f;
    --white: #ffffff;
    --accent-orange: #f8a61f;
    --cta-red: #e3262a;
    --plane-glow: rgba(233, 240, 248, 0.55);
    --plane-fade: rgba(233, 240, 248, 0);
  }
  * { margin: 0; padding: 0; box-sizing: border-box; }
  html, body { width: 1200px; height: 148px; overflow: hidden; background: var(--white); }
  body { font-family: "Open Sans", Arial, sans-serif; }

  .banner {
    position: relative;
    width: 1200px;
    height: 148px;
    overflow: hidden;
    background: linear-gradient(100deg, var(--sky-light) 0%, var(--sky-mid) 40%, var(--sky-deep) 72%, var(--sky-deep) 100%);
  }

  .brand {
    position: absolute;
    left: 30px;
    top: 48px;
    height: 52px;
    display: flex;
    align-items: center;
    gap: 10px;
  }
  .brand-dot {
    width: 52px;
    height: 52px;
    border-radius: 50%;
    background: var(--white);
    flex: none;
  }
  .brand-name {
    color: var(--white);
    font-weight: 800;
    font-size: 25px;
    letter-spacing: 0.3px;
    text-transform: uppercase;
    line-height: 1;
  }

  .plane-visual {
    position: absolute;
    left: 272px;
    top: 0;
    width: 400px;
    height: 148px;
    background: radial-gradient(ellipse 55% 45% at 52% 58%, var(--plane-glow) 0%, var(--plane-fade) 100%);
  }

  .badge {
    position: absolute;
    left: 707px;
    top: 11px;
    width: 126px;
    height: 126px;
    border-radius: 50%;
    background: var(--badge);
    display: flex;
    align-items: center;
    justify-content: center;
    text-align: center;
    color: var(--white);
    font-weight: 700;
    font-size: 12.5px;
    line-height: 1.5;
    text-transform: uppercase;
  }

  .headline {
    color: var(--white);
    font-weight: 800;
    text-transform: uppercase;
  }
  .headline-top,
  .headline-bottom {
    position: absolute;
    left: 849px;
    line-height: 1;
    white-space: nowrap;
  }
  .headline-top {
    top: 30px;
    font-size: 31px;
    letter-spacing: 0.6px;
  }
  .headline-top .accent { color: var(--accent-orange); }
  .headline-bottom {
    top: 77px;
    font-size: 36px;
  }

  .cta {
    position: absolute;
    left: 1025px;
    top: 74px;
    width: 147px;
    height: 45px;
    background: var(--cta-red);
    color: var(--white);
    font-weight: 700;
    font-size: 17px;
    text-transform: uppercase;
    display: flex;
    align-items: center;
    justify-content: center;
    text-decoration: none;
  }
</style>
</head>
<body>
  <div class="banner">
    <div class="brand">
      <span class="brand-dot"></span>
      <span class="brand-name">Wingmerry</span>
    </div>

    <div class="plane-visual" role="img" aria-label="Photo of a white passenger airliner flying through a blue sky"></div>

    <div class="badge">Unique flight<br>combinations</div>

    <h1 class="headline">
      <span class="headline-top">Find the <span class="accent">cheapest</span></span>
      <span class="headline-bottom">Flights!</span>
    </h1>

    <a class="cta" href="#">Find now!</a>
  </div>
</body>
</html>
```